Rebrand/migrate of website to Wordpress

Rebrand/transfer of php website to new wordpress website using the Corvix theme. Dial4LowerRates.com is being rebranded to Quarnix and therefore we are looking to simplify the current layout to match competitors sites and be mobile device friendly.
The new site will need to show services in a clear uncluttered way with more emphasis on the service rather than large amounts of text. See attachment B1 for example.
Competitors sites are qm.com , chatwave.co.uk, vlinkup.com
Updates

As I have had a few request from designers to extend the deadline. I have requested Pixel Forum to extend to Tuesday 3rd April 2018

Target Market(s)

UK Home phone and small business customers

Industry/Entity Type

Telecom

Coding

Coded - Design and coding required

Number of Pages Required

5+ page

Colors

Designer to choose colors to be used in the design.

Requirements
Must have
• 1. Use Corvix wordpress theme that will be supplied.
• 2. Combine the best layouts where possible as used by competitors but in a unique way.
• 3. Horizontal bar should be in white so that it can layer over banner as per file A1.
• 4. Simplify current layout to match competitors see attached file B1.
• 5. Integrate Glintcraft - Glintleads for Web / web form to capture interested customers - name, Company name, Telephone number, email address.
Should not have
• Colour scheme that is the same as our competitors ChatWave, QM, Harbor, Dura Link

```html
<!DOCTYPE html>
<html lang="en">
<head>
<meta charset="utf-8">
<title>Dial4LowerRates – Cheaper Calls</title>
<link rel="stylesheet" href="https://fonts.googleapis.com/css2?family=Roboto+Condensed:wght@300;400;700&family=Poppins:wght@400;500;600&display=swap">
<style>
:root{
  --cyan:#05b2e4;
  --cyan-light:#9fe0f3;
  --orange:#f7901e;
  --orange-soft:#fde3cc;
  --magenta:#d6136f;
  --dark:#262626;
  --darker:#1d1d1d;
  --ink:#333;
  --muted:#777;
  --white:#fff;
}
*{box-sizing:border-box;margin:0;padding:0}
html,body{width:1200px;height:3267px;overflow:hidden}
body{position:relative;background:var(--white);font-family:"Poppins",sans-serif;color:var(--ink)}
.abs{position:absolute}
.center{text-align:center;left:0;width:1200px}
.heading{font-family:"Roboto Condensed",sans-serif;font-weight:300;font-size:38px;color:var(--ink)}
.heading b{font-weight:700}
.intro{font-size:12px;line-height:27px;color:var(--muted);left:240px;width:720px;text-align:center}
.btn{display:flex;align-items:center;justify-content:center;border-radius:26px;font-size:11px;font-weight:600;text-transform:uppercase;letter-spacing:.5px}

/* hero */
.hero-photo{left:0;top:0;width:1200px;height:720px;background:linear-gradient(100deg,#5a4a3a 0%,#8a7360 35%,#c9a58a 65%,#6b5444 100%)}
.topbar{left:113px;top:17px;width:976px;height:103px;background:rgba(30,30,30,.92)}
.phone-order{left:130px;top:36px;color:var(--white);font-size:13px;font-weight:600}
.phone-order span{font-size:17px;margin-left:10px}
.brand-tab{left:478px;top:17px;width:300px;height:56px;background:var(--white);display:flex;align-items:center;justify-content:center;gap:8px;border-radius:0 0 10px 10px}
.brand-tab .mark{width:18px;height:18px;background:var(--cyan)}
.brand-name{font-family:"Poppins",sans-serif;font-weight:500;font-size:22px;color:#3a3a3a}
.social-top{top:36px;width:14px;height:14px;border-radius:50%;background:var(--cyan)}
.account{left:975px;top:36px;color:var(--white);font-size:11px;font-weight:600;text-transform:uppercase}
.nav{left:113px;top:84px;width:976px;display:flex;justify-content:flex-start;gap:0;padding-left:208px}
.nav a{color:var(--white);text-decoration:none;font-size:11px;font-weight:500;text-transform:uppercase;margin-right:52px}
.nav a.active{color:var(--orange)}
.hero-title{left:113px;top:222px;font-family:"Roboto Condensed",sans-serif;font-weight:700;font-size:60px;line-height:70px;color:var(--cyan)}
.hero-text{left:113px;top:380px;width:520px;color:var(--white);font-size:16px;line-height:35px;font-weight:500}
.hero-btn{left:113px;top:514px;width:148px;height:48px;background:var(--orange);color:var(--white)}

/* plans */
.plans-band{left:0;top:640px;width:1200px;height:680px}
.plan-card{top:884px;width:308px;height:300px;background:var(--white);text-align:center;box-shadow:0 4px 14px rgba(0,0,0,.08)}
.plan-card h3{margin-top:30px;font-family:"Roboto Condensed",sans-serif;font-weight:700;font-size:27px;color:var(--orange)}
.plan-card p{margin:18px auto 0;width:240px;font-size:11px;line-height:22px;color:var(--muted)}
.price{margin-top:22px;font-family:"Poppins",sans-serif;font-size:44px;color:var(--orange)}
.price small{font-size:11px;color:var(--muted)}
.plan-card .btn{margin:26px auto 0;width:124px;height:40px;border:1px solid var(--orange);color:var(--orange);text-transform:none;font-weight:500}
.plan-card.featured{background:var(--orange)}
.plan-card.featured h3,.plan-card.featured .price,.plan-card.featured p,.plan-card.featured small{color:var(--white)}
.plan-card.featured .btn{border-color:var(--white);color:var(--white)}

/* started */
.start-card{top:1535px;width:394px;height:214px;background:var(--white);box-shadow:0 6px 22px rgba(0,0,0,.10)}
.start-card .circle{left:0;top:60px;width:92px;height:92px;border-radius:50%;background:#f2f2f2;display:flex;align-items:center;justify-content:center}
.start-card h3{left:102px;top:30px;font-family:"Roboto Condensed",sans-serif;font-weight:700;font-size:25px}
.start-card p{left:102px;top:66px;width:260px;font-size:12px;line-height:24px;color:var(--muted)}
.start-card .btn{left:102px;top:135px;width:126px;height:40px;font-weight:500}
.biz h3{color:var(--orange)} .biz .btn{border:1px solid var(--orange);color:var(--ink)}
.res h3{color:var(--cyan)} .res .btn{border:1px solid var(--cyan);color:var(--ink)}

/* refer */
.refer-photo{left:545px;top:1890px;width:655px;height:440px;background:linear-gradient(110deg,#b98f6d 0%,#6f4a3a 40%,#d47e6a 70%,#a63a6a 100%)}
.refer-line{left:113px;font-family:"Roboto Condensed",sans-serif;font-weight:400;font-size:41px;color:var(--white)}
.refer-free{left:113px;top:2110px;font-family:"Roboto Condensed",sans-serif;font-weight:700;font-size:50px;color:var(--magenta)}
.refer-btn{left:113px;top:2202px;width:148px;height:48px;border:2px solid var(--white);color:var(--white)}

/* reviews */
.review{width:308px;height:190px;background:var(--white);box-shadow:0 4px 18px rgba(0,0,0,.10)}
.review .stars{left:18px;top:22px;display:flex;gap:2px}
.review .date{right:18px;top:22px;font-size:11px;color:var(--muted)}
.review p{left:30px;width:248px;top:62px;font-size:11px;line-height:24px;color:var(--muted);text-align:center}
.review .who{left:0;width:308px;top:140px;text-align:center;font-size:11px;color:var(--orange)}
.dot{top:2836px;width:9px;height:9px;border-radius:50%}

/* footer */
.footer{left:0;top:2929px;width:1200px;height:338px;background:var(--dark)}
.footer-bottom{left:0;top:3184px;width:1200px;height:83px;background:var(--darker);border-top:1px solid #3a3a3a}
.foot-brand{left:146px;top:2968px;color:var(--white);font-weight:500;font-size:24px}
.foot-about{left:118px;top:3025px;width:300px;text-align:center;color:#bdbdbd;font-size:11px;line-height:24px}
.foot-head{font-family:"Roboto Condensed",sans-serif;font-size:19px;color:var(--white)}
.foot-links{left:499px;top:3010px;list-style:none}
.foot-links li{font-size:11px;line-height:23px;color:#cfcfcf}
.foot-notes{left:680px;top:3010px;width:410px;font-size:11px;line-height:23px;color:#cfcfcf}
.foot-divider{top:2960px;width:1px;height:190px;background:#3a3a3a}
.social-foot{top:3207px;width:34px;height:34px;border-radius:50%;background:var(--white)}
.newsletter{left:490px;top:3207px;width:220px;height:34px;border-radius:17px;background:var(--white);overflow:hidden}
.newsletter .go{position:absolute;right:0;top:0;width:56px;height:34px;background:var(--magenta);color:var(--white);font-size:13px;font-weight:600;display:flex;align-items:center;justify-content:center;border-radius:17px}
.copyright{left:925px;top:3218px;font-size:11px;color:#cfcfcf}
</style>
</head>
<body>

<!-- hero -->
<div class="abs hero-photo" role="img" aria-label="Photo of a smiling woman in glasses talking on a mobile phone"></div>
<div class="abs topbar"></div>
<div class="abs phone-order">ORDER BY FREE PHONE <span>0800 417 3920</span></div>
<div class="abs brand-tab"><span class="mark"></span><span class="brand-name">dial4lowerrates</span></div>
<span class="abs social-top" style="left:795px"></span>
<span class="abs social-top" style="left:845px"></span>
<div class="abs account">
  <svg width="12" height="12" viewBox="0 0 12 12" style="vertical-align:-1px;margin-right:6px"><circle cx="6" cy="3.5" r="3" fill="#fff"/><path d="M0 12a6 5 0 0 1 12 0z" fill="#fff"/></svg>My Account
</div>
<nav class="abs nav">
  <a class="active">Home</a><a>About Us</a><a>Business</a><a>Residential</a><a>Support</a><a>Contact</a>
</nav>
<h1 class="abs hero-title">Switch To<br>Cheaper Calls Now !</h1>
<p class="abs hero-text">Make Cheap LOCAL, NATIONAL &amp; INTERNATIONAL Unlimited Phone Calls To Your Friends, Family And More With Our Great Calling Plans.</p>
<div class="abs btn hero-btn">Start Here</div>

<!-- plans band -->
<svg class="abs plans-band" viewBox="0 0 1200 680" preserveAspectRatio="none">
  <path d="M0 40 C200 80 350 -10 560 25 C760 60 900 20 1200 45 L1200 680 L0 680Z" fill="#05b2e4"/>
  <path d="M0 560 C250 600 420 500 650 545 C850 585 1000 520 1200 560 L1200 680 L0 680Z" fill="#9fe0f3"/>
  <path d="M0 590 C250 660 450 600 700 630 C900 655 1050 610 1200 640 L1200 680 L0 680Z" fill="#fff"/>
</svg>
<h2 class="abs center heading" style="top:735px;color:#fff">Choose <b>Your Plans</b></h2>
<p class="abs intro" style="top:790px;color:#fff">Lorem ipsum dolor sit amet, consectetuer adipiscing elit, sed diam nonummy nibh euismod tincidunt ut laoreet dolore magna aliquam erat volutpat. Ut wisi enim ad minim veniam, quis ullamcorper suscipit lobortis .</p>

<div class="abs plan-card" style="left:113px">
  <h3>Home Saver</h3>
  <p>Unlimited Local &amp; National evening &amp; Weeend calls for just</p>
  <div class="price">£ 2.99<small>/Month</small></div>
  <div class="btn">Know More</div>
</div>
<div class="abs plan-card featured" style="left:446px">
  <h3>Home Saver Anytime</h3>
  <p>Unlimited Local &amp; National evening &amp; Weeend calls for just</p>
  <div class="price">£ 9.99<small>/Month</small></div>
  <div class="btn">Know More</div>
</div>
<div class="abs plan-card" style="left:780px">
  <h3>Home Saver International</h3>
  <p>Unlimited Local &amp; National evening &amp; Weeend calls for just</p>
  <div class="price">£ 14.99<small>/Month</small></div>
  <div class="btn">Know More</div>
</div>

<!-- get started -->
<h2 class="abs center heading" style="top:1386px">Ready to <b>Get Started</b></h2>
<p class="abs intro" style="top:1440px">Lorem ipsum dolor sit amet, consectetuer adipiscing elit, sed diam nonummy nibh euismod tincidunt ut laoreet dolore magna aliquam erat volutpat. Ut wisi enim ad minim veniam, quis ullamcorper suscipit lobortis .</p>

<div class="abs start-card biz" style="left:192px">
  <div class="abs circle" style="left:-30px">
    <svg width="34" height="28" viewBox="0 0 34 28"><rect x="11" y="1" width="12" height="6" rx="2" fill="none" stroke="#f7901e" stroke-width="2.5"/><rect x="1" y="6" width="32" height="21" rx="3" fill="#f7901e"/><rect x="1" y="14" width="32" height="2" fill="#fff"/></svg>
  </div>
  <h3 class="abs">FOR BUSINESS</h3>
  <p class="abs">Lorem ipsum dolor sit amet, consectetuer adipiscing elit, sed dia.</p>
  <div class="abs btn">Get Started Now</div>
</div>
<div class="abs start-card res" style="left:660px">
  <div class="abs circle" style="left:-30px">
    <svg width="34" height="32" viewBox="0 0 34 32"><path d="M17 1 L33 13 H1Z" fill="#05b2e4"/><rect x="4" y="13" width="26" height="18" fill="#05b2e4"/><rect x="9" y="17" width="5" height="5" fill="#fff"/><rect x="20" y="17" width="5" height="5" fill="#fff"/><rect x="14" y="24" width="6" height="7" fill="#fff"/></svg>
  </div>
  <h3 class="abs">FOR RESIDENTIAL</h3>
  <p class="abs">Lorem ipsum dolor sit amet, consectetuer adipiscing elit, sed dia.</p>
  <div class="abs btn">Get Started Now</div>
</div>

<!-- refer a friend -->
<svg class="abs" style="left:0;top:1860px" width="1200" height="500" viewBox="0 0 1200 500">
  <path d="M0 20 C200 -10 380 60 600 40 C820 20 980 -10 1200 20 L1200 480 C980 430 820 500 600 470 C380 440 200 500 0 460Z" fill="#fde3cc"/>
  <path d="M0 45 C200 15 380 85 600 65 C820 45 980 15 1200 45 L1200 455 C980 405 820 475 600 445 C380 415 200 475 0 435Z" fill="#f7901e"/>
</svg>
<div class="abs refer-photo" role="img" aria-label="Photo of two young women laughing while looking at a phone" style="clip-path:path('M0 60 C120 30 250 20 420 10 C520 5 600 20 655 30 L655 420 C560 380 420 440 250 425 C140 415 60 440 0 430Z')"></div>
<div class="abs refer-line" style="top:1985px">REFER A FRIEND AND</div>
<div class="abs refer-line" style="top:2044px">GET 2 MONTHS</div>
<div class="abs refer-free">FREE CALL PACKAGE</div>
<div class="abs btn refer-btn">Start Here</div>

<!-- reviews -->
<h2 class="abs center heading" style="top:2425px">Customer <b>Review</b></h2>
<p class="abs intro" style="top:2479px">Lorem ipsum dolor sit amet, consectetuer adipiscing elit, sed diam nonummy nibh euismod tincidunt ut laoreet dolore magna aliquam erat volutpat. Ut wisi enim ad minim veniam, quis nostrud exerci tation ullamcorper suscipit lobortis .</p>

<div class="abs review" style="left:113px;top:2581px">
  <div class="abs stars"><svg width="82" height="14" viewBox="0 0 82 14"><g fill="#f5c518"><path id="st" d="M7 0l2 5h5l-4 3 1.5 5L7 10 2.5 13 4 8 0 5h5z"/><use href="#st" x="17"/><use href="#st" x="34"/><use href="#st" x="51"/><use href="#st" x="68"/></g></svg></div>
  <div class="abs date">26.03.2018</div>
  <p class="abs">I'm more likely to just pick up the phone... Instead of using email, I now speak to people. just pick up the phone...</p>
  <div class="abs who">Marcus T, Cornwall</div>
</div>
<div class="abs review" style="left:446px;top:2566px;height:222px">
  <div class="abs stars"><svg width="82" height="14" viewBox="0 0 82 14"><g fill="#f5c518"><use href="#st"/><use href="#st" x="17"/><use href="#st" x="34"/><use href="#st" x="51"/><use href="#st" x="68"/></g></svg></div>
  <div class="abs date">26.03.2018</div>
  <p class="abs" style="top:76px">I'm more likely to just pick up the phone... Instead of using email, I now speak to people. just pick up the phone...</p>
  <div class="abs who" style="top:160px">Marcus T, Cornwall</div>
</div>
<div class="abs review" style="left:780px;top:2581px">
  <div class="abs stars"><svg width="82" height="14" viewBox="0 0 82 14"><g fill="#f5c518"><use href="#st"/><use href="#st" x="17"/><use href="#st" x="34"/><use href="#st" x="51"/><use href="#st" x="68"/></g></svg></div>
  <div class="abs date">26.03.2018</div>
  <p class="abs">I'm more likely to just pick up the phone... Instead of using email, I now speak to people. just pick up the phone...</p>
  <div class="abs who">Marcus T, Cornwall</div>
</div>
<span class="abs dot" style="left:566px;background:var(--magenta)"></span>
<span class="abs dot" style="left:583px;background:var(--cyan)"></span>
<span class="abs dot" style="left:600px;background:var(--orange)"></span>
<span class="abs dot" style="left:617px;background:#555"></span>

<!-- footer -->
<footer>
  <div class="abs footer"></div>
  <div class="abs foot-brand">dial4lowerrates</div>
  <p class="abs foot-about">Lorem ipsum dolor sit amet, consectetuer adipiscing elit, sed diam nonummy nibh euismod tincidunt ut laoreet dolore magna aliquam erat volutpat. nibh euismod tincidunt.</p>
  <span class="abs foot-divider" style="left:460px"></span>
  <span class="abs foot-divider" style="left:640px"></span>
  <div class="abs foot-head" style="left:499px;top:2972px">Company</div>
  <ul class="abs foot-links"><li>Home</li><li>About Us</li><li>Business</li><li>Residential</li><li>Support</li><li>Contact</li></ul>
  <div class="abs foot-head" style="left:680px;top:2972px">Notes For You</div>
  <p class="abs foot-notes">1.Applies to UK landline numbers starting with 01, 02 and 03. International landlines calls to countries in our call plans are unlimited and do not include calls to mobiles unless specified.<br>Calls are billed on a per second increment. Fair usage policy applies.</p>
  <div class="abs footer-bottom"></div>
  <span class="abs social-foot" style="left:110px"></span>
  <span class="abs social-foot" style="left:163px"></span>
  <div class="abs newsletter"><span class="go">GO</span></div>
  <div class="abs copyright">© All Rights Reserved 2018.</div>
</footer>

</body>
</html>
```